RIPTALON boardgrip need a Packaging Design Boxes for brand new label of wax

You could be the designer of the biggest surfboard wax brand ever.

We need a new packaging design for a new brand based in near Sydney Australia. The Coal Coast. We are called RIPTALON boardgrip. Packaging is to be a Folding box using recycled paper/cardboard. It must hold 100 grams of wax. So the box must be around 8 cms x 8 cms x 3 cms in height.The box blue print lay out is needed for printing.Our surfboard wax comes in 5 scents including Coconut / Lime, Mango, Passionfruit, Bubblegum and Strawberry / Cream. Our scented wax is unique in this industry by our range of scents. And aslo hand made in Australia. The wax comes in 4 water temperatures Tropical, Warm, Cool and Cold. So 5 individual scented boxes with a 4 generic water temperatures temple on each.
The name riptalon refers to the colloquial sporting
term that is used when the rider has successfully completed a maneuver- such as ' he totally riptalon that move'. Although we do link the brand name riptalon to the scents and green initiatives in the making of our product. Also packaging must say things like Made on The Coal Coast NSW Australia, Do not Eat, 100 grams, Hand Made, What scent it is, Store in cool place, template for water temperature and a area for a bar code

Target Market(s)

Surfing, surfer is the target customers age from 10 years and up. Both male and female. This is a very new brand about to hit the east coast of Australia.

Industry/Entity Type

Industry

Requirements
Must have
• The box must hold a round block of surfboard wax. 8 cms in diameter and 2.8 cms in height. Open to printed color or browm box.
Nice to have
• The name RIPTALON boardgrip is the name. Hold fast and ride tall, is the catch phrase.100 grams and a water temperature measurement gauge for the 4 tropical, warm, cool and cold. Which can be used by me marking it when needed.Top of box wax comes in 6 fragrance so will need 1 for each scent .Hand made on the Coal Coast NSW.
Trying for a tuff stance kind of look
Should not have
• This is a surfboard wax not hair wax or anything.
So not girlllly

```html
<!DOCTYPE html>
<html lang="en">
<head>
<meta charset="utf-8">
<title>RIPTALON boardgrip – Mango box</title>
<link rel="stylesheet" href="https://fonts.googleapis.com/css2?family=Montserrat:wght@200;300;400;600;700;800&family=Open+Sans:wght@400;600&display=swap">
<style>
  :root {
    --bg: #ececec;
    --panel: #ffffff;
    --side: #f3f3f3;
    --orange: #f29a16;
    --orange-text: #e8890f;
    --brown: #3a2414;
    --ink: #2a1a10;
    --body: #222222;
    --gold-dark: #8a5a05;
    --gold: #d9a019;
  }
  * { margin: 0; padding: 0; box-sizing: border-box; }
  html, body { width: 1200px; height: 1200px; overflow: hidden; background: var(--bg); }
  .canvas { position: relative; width: 1200px; height: 1200px; font-family: "Montserrat", sans-serif; }

  /* ---------- side panel (300 x 800, artwork rotated) ---------- */
  .box-side {
    position: absolute; left: 50px; top: 200px; width: 300px; height: 800px;
    background: var(--side); overflow: hidden;
    box-shadow: 0 20px 50px rgba(0,0,0,.10);
  }
  .side-art {
    position: absolute; left: -250px; top: 250px; width: 800px; height: 300px;
    transform: rotate(90deg);
  }
  .side-brand {
    position: absolute; left: 420px; top: 22px; width: 210px; height: 80px;
    background: var(--orange); color: #fff; border-radius: 3px;
    display: flex; flex-direction: column; justify-content: center; padding: 0 14px;
  }
  .side-brand-name { font-weight: 800; font-size: 34px; line-height: 1; white-space: nowrap; }
  .side-brand-tag { align-self: flex-end; font-family: "Open Sans", sans-serif; font-weight: 600; font-size: 11px; }
  .side-scent {
    position: absolute; left: 640px; top: 22px; width: 145px; height: 62px;
    background: var(--brown); color: #fff; border-radius: 4px;
    display: flex; align-items: center; justify-content: center;
    font-weight: 800; font-size: 32px;
  }
  .side-photo {
    position: absolute; left: 640px; top: 100px; width: 145px; height: 80px;
    background: radial-gradient(ellipse at center, #f4b81c 0%, #f0c550 55%, var(--side) 72%);
  }
  .side-temps {
    position: absolute; left: 20px; top: 118px; width: 400px;
    display: grid; grid-template-columns: 220px 180px; row-gap: 6px; list-style: none;
  }
  .side-temp { display: flex; align-items: center; gap: 10px; color: var(--orange-text); font-weight: 700; font-size: 20px; }
  .side-temp-box { width: 16px; height: 16px; border: 2px solid var(--orange-text); border-radius: 2px; }
  .side-weight { position: absolute; left: 20px; top: 182px; font-weight: 300; font-size: 28px; color: var(--ink); }
  .side-handmade { position: absolute; left: 20px; top: 216px; font-weight: 200; font-size: 34px; color: var(--ink); letter-spacing: -1px; }
  .side-origin { position: absolute; left: 20px; top: 264px; font-weight: 700; font-size: 12px; color: var(--ink); }

  /* ---------- front panel (800 x 800) ---------- */
  .box-front {
    position: absolute; left: 350px; top: 200px; width: 800px; height: 800px;
    background: linear-gradient(180deg, #ffffff 0%, #f6f6f6 100%);
    border-left: 1px solid #dcdcdc;
    box-shadow: 0 20px 50px rgba(0,0,0,.12);
    overflow: hidden;
  }
  .brand-banner {
    position: absolute; left: 170px; top: 20px; width: 460px; height: 160px;
    background: var(--orange); color: #fff; border-radius: 4px;
    display: flex; flex-direction: column; justify-content: center; padding: 0 30px;
  }
  .brand-name { font-weight: 800; font-size: 72px; line-height: 1; white-space: nowrap; }
  .brand-tag { align-self: flex-end; font-family: "Open Sans", sans-serif; font-weight: 600; font-size: 20px; margin-top: 4px; }
  .scent-pill {
    position: absolute; left: 225px; top: 200px; width: 350px; height: 100px;
    background: var(--brown); color: #fff; border-radius: 6px;
    display: flex; align-items: center; justify-content: center;
    font-weight: 800; font-size: 68px; letter-spacing: -1px;
  }
  .blurb {
    position: absolute; left: 40px; top: 318px; width: 720px;
    font-family: "Open Sans", sans-serif; font-size: 15px; line-height: 1.45;
    color: var(--body); text-align: center; letter-spacing: -.2px;
  }
  .hero-photo {
    position: absolute; left: 300px; top: 450px; width: 500px; height: 330px;
    background: linear-gradient(160deg, #f1ddc8 0%, #e9c9a8 55%, #f3e4a0 80%, #f1b92a 100%);
    opacity: .9;
  }
  .temp-list { position: absolute; left: 30px; top: 420px; list-style: none; }
  .temp-item {
    display: flex; align-items: center; gap: 14px; height: 50px;
    color: var(--orange-text); font-weight: 700; font-size: 34px;
  }
  .temp-box { width: 26px; height: 26px; border: 3px solid var(--orange-text); border-radius: 3px; background: #fff; }
  .weight { position: absolute; left: 30px; top: 625px; font-weight: 300; font-size: 38px; color: var(--ink); letter-spacing: -1px; line-height: 1; }
  .new-badge { position: absolute; left: 620px; top: 440px; width: 150px; height: 150px; }
  .handmade { position: absolute; left: 30px; top: 680px; font-weight: 200; font-size: 62px; color: var(--ink); letter-spacing: -2px; line-height: 1; }
  .origin { position: absolute; left: 30px; top: 752px; font-weight: 700; font-size: 18px; color: var(--ink); }
</style>
</head>
<body>
<div class="canvas">
  <aside class="box-side">
    <div class="side-art">
      <div class="side-brand">
        <span class="side-brand-name">RIPTALON</span>
        <span class="side-brand-tag">boardgrip</span>
      </div>
      <div class="side-scent">MANGO</div>
      <div class="side-photo" role="img" aria-label="Photo of halved mangoes"></div>
      <ul class="side-temps">
        <li class="side-temp"><span class="side-temp-box"></span>TROPICAL</li>
        <li class="side-temp"><span class="side-temp-box"></span>COOL</li>
        <li class="side-temp"><span class="side-temp-box"></span>WARM</li>
        <li class="side-temp"><span class="side-temp-box"></span>COLD</li>
      </ul>
      <div class="side-weight">100 GRAMS</div>
      <div class="side-handmade">HAND MADE</div>
      <div class="side-origin">MADE ON THE COAL COAST NSW AUSTRALIA</div>
    </div>
  </aside>

  <section class="box-front">
    <div class="brand-banner">
      <span class="brand-name">RIPTALON</span>
      <span class="brand-tag">boardgrip</span>
    </div>
    <div class="scent-pill">MANGO</div>
    <p class="blurb">Lorem ipsum dolor sit amet, consectetur adipisicing elit, sed do eiusmod tempor incididunt ut labore et dolore magna aliqua. Ut enim ad minim veniam, quis nostrud exercitation. Lorem ipsum dolor sit amet, consectetur adipisicing elit, sed do eiusmod tempor incididunt ut labore et dolore magna aliqua. Ut enim ad minim veniam, quis nostrud exercitation.</p>

    <div class="hero-photo" role="img" aria-label="Photo of bare legs with a sheer yellow wrap and halved mangoes"></div>

    <ul class="temp-list">
      <li class="temp-item"><span class="temp-box"></span>TROPICAL</li>
      <li class="temp-item"><span class="temp-box"></span>WARM</li>
      <li class="temp-item"><span class="temp-box"></span>COOL</li>
      <li class="temp-item"><span class="temp-box"></span>COLD</li>
    </ul>
    <div class="weight">100 GRAMS</div>

    <svg class="new-badge" viewBox="0 0 200 200" aria-label="New">
      <polygon fill="var(--gold-dark)" points="100,5 116,35 148,20 150,55 185,55 170,85 198,105 168,122 180,155 145,155 140,190 110,172 100,198 88,172 58,190 55,155 20,158 32,122 2,105 30,85 15,55 50,55 52,20 84,35"/>
      <circle cx="100" cy="100" r="62" fill="var(--gold)"/>
      <text x="100" y="114" text-anchor="middle" transform="rotate(-25 100 100)" font-family="Montserrat, sans-serif" font-weight="800" font-size="44" fill="#ffffff">NEW</text>
    </svg>

    <div class="handmade">HAND MADE</div>
    <div class="origin">MADE ON THE COAL COAST NSW AUSTRALIA</div>
  </section>
</div>
</body>
</html>
```